Brightwater Medical business cards

Double sided business cards.

Medical technology consulting company.

Business cards with two names on the front, upper to middle left:

Dr Colin R. Haskell MBBS FRACP +61491578204
Dr Paul Brennagh PhD MBusAdmin +61472019847

Email and website addresses bottom right:

colin@brightwatermedical.com.au
www.brightwatermedical.com.au

Tree logo (as per attached file) on front in a suitable position.

Tag line (as per attached files) on the back.

Need a file format to upload to Desk Ford or Cardmoor.

```html
<!DOCTYPE html>
<html lang="en">
<head>
<meta charset="utf-8">
<title>Brightwater Medical — Business Cards</title>
<link rel="stylesheet" href="https://fonts.googleapis.com/css2?family=Lato:wght@400;700&display=swap">
<style>
  :root {
    --backdrop: #737373;
    --cream: #fef3d6;
    --leaf-green: #86aa42;
    --brand-green: #5a8a14;
    --white: #ffffff;
    --leaf-pale: rgba(255, 255, 255, 0.28);
    --shadow: rgba(0, 0, 0, 0.35);
  }
  * { margin: 0; padding: 0; box-sizing: border-box; }
  html, body {
    width: 1200px; height: 1000px; overflow: hidden;
    background: var(--backdrop);
    font-family: "Lato", Arial, sans-serif;
  }
  .canvas { position: relative; width: 1200px; height: 1000px; }

  .card {
    position: absolute; width: 613px; height: 352px;
    box-shadow: 14px 14px 22px var(--shadow);
    overflow: hidden;
  }
  .card--back {
    left: 195px; top: 101px;
    background: var(--cream);
    border-radius: 52px 0 52px 0;
  }
  .card--front {
    left: 375px; top: 506px;
    background: var(--leaf-green);
    border-radius: 0 52px 0 52px;
    color: var(--white);
  }

  /* Brand lockup */
  .brand { position: absolute; text-align: center; }
  .brand__dot { display: block; margin: 0 auto; border-radius: 50%; }
  .brand__name { font-weight: 400; letter-spacing: 0.3px; white-space: nowrap; }
  .brand__tagline { white-space: nowrap; }
  .brand__tagline .sep { font-size: 0.75em; padding: 0 2px; }

  .card--back .brand { left: 0; right: 0; top: 105px; }
  .card--back .brand__dot { width: 76px; height: 76px; background: var(--brand-green); margin-bottom: 36px; }
  .card--back .brand__name { font-size: 29px; color: var(--brand-green); line-height: 34px; }
  .card--back .brand__tagline { font-size: 15.5px; color: var(--brand-green); margin-top: 3px; }

  .card--front .brand { left: 290px; width: 270px; top: 74px; }
  .card--front .brand__dot { width: 60px; height: 60px; background: var(--white); margin-bottom: 36px; }
  .card--front .brand__name { font-size: 21.5px; line-height: 26px; }
  .card--front .brand__tagline { font-size: 11.5px; margin-top: 3px; }

  /* Decorative leaf strip */
  .leaf-strip {
    position: absolute; left: 0; top: 0; width: 110px; height: 352px;
    background: linear-gradient(90deg, var(--leaf-pale), rgba(255,255,255,0));
  }

  /* Contacts */
  .people { position: absolute; right: 363px; top: 57px; text-align: right; }
  .person + .person { margin-top: 16px; }
  .person__name { font-weight: 700; font-size: 17px; line-height: 22px; }
  .person__creds, .person__phone { font-size: 16.5px; line-height: 21px; }
  .person__phone svg { width: 11px; height: 11px; margin-right: 4px; vertical-align: -1px; }

  .links { position: absolute; right: 66px; top: 281px; text-align: right; font-size: 14px; line-height: 20px; }
  .links svg { width: 12px; height: 12px; margin-left: 7px; vertical-align: -1px; }
</style>
</head>
<body>
<main class="canvas">

  <section class="card card--back" aria-label="Card back">
    <div class="brand">
      <span class="brand__dot"></span>
      <div class="brand__name">BRIGHTWATER MEDICAL</div>
      <div class="brand__tagline">Insight <span class="sep">|</span> Development <span class="sep">|</span> Onward</div>
    </div>
  </section>

  <section class="card card--front" aria-label="Card front">
    <div class="leaf-strip" role="img" aria-label="Faint decorative leaves along the left edge"></div>

    <div class="people">
      <div class="person">
        <div class="person__name">Dr. Colin R. Haskell</div>
        <div class="person__creds">MBBS FRACP</div>
        <div class="person__phone"><svg viewBox="0 0 24 24"><path fill="#fff" d="M6.6 10.8a15 15 0 0 0 6.6 6.6l2.2-2.2a1 1 0 0 1 1-.25 11.4 11.4 0 0 0 3.6.57 1 1 0 0 1 1 1V20a1 1 0 0 1-1 1A17 17 0 0 1 3 4a1 1 0 0 1 1-1h3.5a1 1 0 0 1 1 1c0 1.25.2 2.45.57 3.57a1 1 0 0 1-.25 1z"/></svg>+61491578204</div>
      </div>
      <div class="person">
        <div class="person__name">Dr. Paul Brennagh</div>
        <div class="person__creds">PhD MBusAdmin</div>
        <div class="person__phone"><svg viewBox="0 0 24 24"><path fill="#fff" d="M6.6 10.8a15 15 0 0 0 6.6 6.6l2.2-2.2a1 1 0 0 1 1-.25 11.4 11.4 0 0 0 3.6.57 1 1 0 0 1 1 1V20a1 1 0 0 1-1 1A17 17 0 0 1 3 4a1 1 0 0 1 1-1h3.5a1 1 0 0 1 1 1c0 1.25.2 2.45.57 3.57a1 1 0 0 1-.25 1z"/></svg>+61472019847</div>
      </div>
    </div>

    <div class="brand">
      <span class="brand__dot"></span>
      <div class="brand__name">BRIGHTWATER MEDICAL</div>
      <div class="brand__tagline">Insight <span class="sep">|</span> Development <span class="sep">|</span> Onward</div>
    </div>

    <div class="links">
      <div>colin@brightwatermedical.com.au<svg viewBox="0 0 24 24"><rect x="2" y="5" width="20" height="14" fill="#fff"/><path d="M2 5l10 8 10-8" fill="none" stroke="#86aa42" stroke-width="2"/></svg></div>
      <div>www.brightwatermedical.com.au<svg viewBox="0 0 24 24" fill="none" stroke="#fff" stroke-width="2"><circle cx="12" cy="12" r="10"/><path d="M2 12h20M12 2c3 3 3 17 0 20M12 2c-3 3-3 17 0 20"/></svg></div>
    </div>
  </section>

</main>
</body>
</html>
```